1 Page Sales Brochure of our Services

I need to create a one page brochure that our sales team can take into meetings about our services - Need this to be an impressive one page that looks fresh and new using our brand colors of Brindle green, black and white. Our brand looks "clean" think Marlo brand in how everything is clean and white and crisp. Our website showcases our services: https://brindlesports.example/services/ --- After done with this project I would like to create a full booklet. Want to begin with this project first.

Target Market(s)

State of Texas

Industry/Entity Type

Sports Construction in Texas Only

Font styles to use
Serif

Colors
00AB8E
00BBA5
67D7C9
C6EFE9
E9F9F6

Requirements
Must have
• Front and Back and cover our services outlined on our website: https://brindlesports.example/services/
Nice to have
• Need one that can get sent digital and printed -- Our colors are the Brindle green, white and black - We want brochure to look clean, almost like the Marlo feel of their product's branding

```html
<!DOCTYPE html>
<html lang="en">
<head>
<meta charset="utf-8">
<title>Brindle Sports Construction – Services Brochure</title>
<link href="https://fonts.googleapis.com/css2?family=Oswald:wght@300;400&family=Open+Sans:wght@400;600&display=swap" rel="stylesheet">
<style>
  :root{
    --brand-green:#1f7a3c;
    --brand-green-dark:#17632f;
    --ink:#2b2b2b;
    --body:#4a4a4a;
    --paper:#ffffff;
    --tint:#f3f5f4;
    --footer:#3a3a3a;
    --canvas:#e6e8e7;
  }
  *{box-sizing:border-box;margin:0;padding:0}
  html,body{width:1200px;height:900px;overflow:hidden;background:var(--canvas)}
  body{font-family:"Open Sans",sans-serif;color:var(--body);position:relative}

  .sheet{position:absolute;top:75px;width:580px;height:750px;background:var(--paper);
    box-shadow:0 4px 18px rgba(0,0,0,.12);overflow:hidden}
  .sheet--front{left:13px}
  .sheet--back{left:607px}

  .heading{font-family:"Oswald",sans-serif;font-weight:300;color:var(--ink);text-transform:uppercase;letter-spacing:.3px}
  .copy{font-size:9px;line-height:1.5;color:var(--body)}
  .photo{position:absolute;border-radius:4px}

  /* front */
  .brand{position:absolute;left:34px;top:34px;display:flex;align-items:center;gap:8px}
  .brand__mark{width:14px;height:14px;background:var(--brand-green)}
  .brand__name{font-family:"Open Sans",sans-serif;font-weight:600;font-size:30px;color:var(--brand-green)}
  .tagline{position:absolute;right:22px;top:30px;font-size:17px}
  .tagline-rule{position:absolute;left:262px;right:0;top:62px;height:5px;background:var(--brand-green)}
  .hero{position:absolute;left:0;top:96px;width:580px;height:258px;
    background:linear-gradient(160deg,#9aa59a 0%,#c9bca4 35%,#a9a9a4 60%,#6f7a70 100%)}
  .hero-rule{position:absolute;left:0;top:354px;width:580px;height:6px;background:var(--brand-green)}
  .services{position:absolute;left:34px;top:376px;width:276px}
  .services .heading{font-size:20px;margin-bottom:4px}
  .services__rule{width:60px;height:2px;background:var(--brand-green);margin-bottom:10px}
  .services .copy+.copy{margin-top:9px}
  .offer{position:absolute;left:318px;top:330px;width:244px;height:212px;background:var(--brand-green);
    border-radius:6px;padding:18px 18px}
  .offer .heading{color:#fff;font-size:19px;margin-bottom:12px}
  .offer__list{list-style:none}
  .offer__item{display:flex;align-items:center;gap:8px;color:#fff;font-size:10.5px;line-height:1.75}
  .offer__item svg{flex:none}
  .gallery{position:absolute;left:34px;top:606px;width:512px;display:flex;justify-content:space-between}
  .gallery__item{width:160px;text-align:center}
  .gallery__photo{height:78px;border-radius:4px}
  .gallery__caption{font-family:"Oswald",sans-serif;font-size:8.5px;color:var(--ink);margin-top:5px;text-transform:uppercase}
  .tone-track{background:linear-gradient(180deg,#9fb3c8 0%,#3e8f3f 45%,#5b2b2b 100%)}
  .tone-grass{background:linear-gradient(180deg,#4d8fd6 0%,#a9c7e6 45%,#6e9a3a 60%,#4d7a2a 100%)}
  .tone-synthetic{background:linear-gradient(135deg,#4c9b3c 0%,#6fb64d 50%,#c0392b 75%,#3d7f32 100%)}

  .footer{position:absolute;left:0;bottom:0;width:580px;height:40px;background:var(--footer);display:flex}
  .footer__web{width:190px;background:var(--brand-green);color:#fff;display:flex;align-items:center;
    gap:6px;padding-left:20px;font-size:12px;white-space:nowrap}
  .footer__dot{width:8px;height:8px;border:1.5px solid #fff;border-radius:50%}
  .footer__info{flex:1;color:#e6e6e6;font-size:7px;display:flex;align-items:center;padding-left:12px;white-space:nowrap}

  /* back */
  .cover{position:absolute;left:0;top:0;width:580px;height:270px;
    background:linear-gradient(170deg,#8fa68a 0%,#b9bcb6 30%,#4c8f3d 50%,#b07a5a 70%,#c9cbc6 100%)}
  .cover-rule{position:absolute;left:0;top:270px;width:580px;height:5px;background:var(--brand-green)}
  .stack{position:absolute;left:30px;top:295px;width:150px}
  .stack .photo{position:static;height:88px;margin-bottom:14px}
  .tone-aerial{background:linear-gradient(180deg,#7d9aa8 0%,#6a8f4a 40%,#b3c27a 100%)}
  .tone-dirt{background:linear-gradient(135deg,#c48a5a 0%,#a9663d 60%,#8a4f2e 100%)}
  .tone-turf{background:linear-gradient(180deg,#b8c4c8 0%,#3f8a37 35%,#2f7a2e 100%)}
  .tone-lights{background:linear-gradient(90deg,#5d7a56 0%,#4a6a45 48%,#8fc26f 52%,#5aa04a 100%)}
  .feature{position:absolute;left:200px;width:355px}
  .feature .heading{font-size:18px;margin-bottom:3px}
  .feature__rule{width:50px;height:2px;background:var(--brand-green);margin-bottom:7px}
  .feature .copy{text-align:justify}
  .feature--grass{top:292px}
  .feature--stadium{top:396px}
  .feature--service{top:500px}
  .feature--lighting{top:604px}
</style>
</head>
<body>

<section class="sheet sheet--front">
  <div class="brand"><span class="brand__mark"></span><span class="brand__name">Brindle</span></div>
  <h2 class="heading tagline">Turnkey Solutions for Sports Construction</h2>
  <div class="tagline-rule"></div>

  <div class="hero" role="img" aria-label="Aerial photo of a stadium field under construction, graded dirt and gravel with equipment"></div>
  <div class="hero-rule"></div>

  <div class="services">
    <h3 class="heading">Services</h3>
    <div class="services__rule"></div>
    <p class="copy">Brindle Sports Construction offers turnkey solutions in the realm of general sports construction. We're committed to excellence in all we do, and we seek to develop lasting relationships with our clients. Brindle is not in the business to win a single job and move on. We are working to earn your trust and business as we want you as a customer for life.</p>
    <p class="copy">At Brindle we have 7 Proverbs we strive to live by. Our #1 proverb is to "Deliver On Our Promises". That is our promise to you that we will strive to deliver on time with the quality and service you expect and deserve on every job.</p>
  </div>

  <div class="offer">
    <h3 class="heading">Our Services Include:</h3>
    <ul class="offer__list">
      <li class="offer__item"><svg width="8" height="7" viewBox="0 0 8 7"><path d="M1 3.5l2 2L7 1" fill="none" stroke="#fff" stroke-width="1.4"/></svg>Track Construction</li>
      <li class="offer__item"><svg width="8" height="7" viewBox="0 0 8 7"><path d="M1 3.5l2 2L7 1" fill="none" stroke="#fff" stroke-width="1.4"/></svg>Natural Grass Fields</li>
      <li class="offer__item"><svg width="8" height="7" viewBox="0 0 8 7"><path d="M1 3.5l2 2L7 1" fill="none" stroke="#fff" stroke-width="1.4"/></svg>Synthetic Field Construction</li>
      <li class="offer__item"><svg width="8" height="7" viewBox="0 0 8 7"><path d="M1 3.5l2 2L7 1" fill="none" stroke="#fff" stroke-width="1.4"/></svg>Stadium Construction</li>
      <li class="offer__item"><svg width="8" height="7" viewBox="0 0 8 7"><path d="M1 3.5l2 2L7 1" fill="none" stroke="#fff" stroke-width="1.4"/></svg>Tennis Court Construction</li>
      <li class="offer__item"><svg width="8" height="7" viewBox="0 0 8 7"><path d="M1 3.5l2 2L7 1" fill="none" stroke="#fff" stroke-width="1.4"/></svg>Service + Maintenance</li>
      <li class="offer__item"><svg width="8" height="7" viewBox="0 0 8 7"><path d="M1 3.5l2 2L7 1" fill="none" stroke="#fff" stroke-width="1.4"/></svg>Stadium Lighting</li>
      <li class="offer__item"><svg width="8" height="7" viewBox="0 0 8 7"><path d="M1 3.5l2 2L7 1" fill="none" stroke="#fff" stroke-width="1.4"/></svg>Surface Maintenance + Repair</li>
    </ul>
  </div>

  <div class="gallery">
    <figure class="gallery__item">
      <div class="gallery__photo tone-track" role="img" aria-label="Photo of a finished football field with running track"></div>
      <figcaption class="gallery__caption">Track Construction</figcaption>
    </figure>
    <figure class="gallery__item">
      <div class="gallery__photo tone-grass" role="img" aria-label="Photo of a natural grass ball field under blue sky"></div>
      <figcaption class="gallery__caption">Natural Grass Fields</figcaption>
    </figure>
    <figure class="gallery__item">
      <div class="gallery__photo tone-synthetic" role="img" aria-label="Photo of a worker laying synthetic turf"></div>
      <figcaption class="gallery__caption">Synthetic Field Construction</figcaption>
    </figure>
  </div>

  <footer class="footer">
    <div class="footer__web"><span class="footer__dot"></span>www.brindlesports.example</div>
    <div class="footer__info">info@brindlesports.example &nbsp;|&nbsp; 418 Cedar Ridge Road, Pine Hollow, Texas 75000 &nbsp;|&nbsp; (555) 010 2468</div>
  </footer>
</section>

<section class="sheet sheet--back">
  <div class="cover" role="img" aria-label="Aerial photo of a large football stadium with green field and seating"></div>
  <div class="cover-rule"></div>

  <div class="stack">
    <div class="photo tone-aerial" role="img" aria-label="Aerial photo of natural grass fields in open land"></div>
    <div class="photo tone-dirt" role="img" aria-label="Aerial photo of stadium ground-up earthworks"></div>
    <div class="photo tone-turf" role="img" aria-label="Photo of a technician servicing synthetic turf"></div>
    <div class="photo tone-lights" role="img" aria-label="Before and after photo of a stadium field under new LED lighting"></div>
  </div>

  <article class="feature feature--grass">
    <h3 class="heading">Natural Grass Fields</h3>
    <div class="feature__rule"></div>
    <p class="copy">Our team operates with specialized equipment allowing massive amounts of dirt to be moved and graded when building natural grass fields. Due to the specialists on our team, we can assist in the design build of your water system to ensure your natural grass will hold the test of time after our installation is complete.</p>
  </article>
  <article class="feature feature--stadium">
    <h3 class="heading">Stadium Construction</h3>
    <div class="feature__rule"></div>
    <p class="copy">We are a true turn-key construction company owned and operated by seasoned professionals who care. From ground-up stadium construction to total lifecycle planning, we provide custom construction solutions through all stages of your projects.</p>
  </article>
  <article class="feature feature--service">
    <h3 class="heading">Service + Maintenance</h3>
    <div class="feature__rule"></div>
    <p class="copy">We provide maintenance services and support for all sports surfaces, helping you protect your investment and extend the life of your synthetic turf, track or tennis court through education, performance testing, and maintenance services.</p>
  </article>
  <article class="feature feature--lighting">
    <h3 class="heading">Stadium Lighting</h3>
    <div class="feature__rule"></div>
    <p class="copy">Take advantage of the energy efficiency and cost savings by converting to LED lighting. According to the US Department of Energy, light-emitting diodes (LED) are six to seven times more energy efficient than conventional light bulbs and cut energy use by more than 80 percent.</p>
  </article>

  <footer class="footer">
    <div class="footer__web"><span class="footer__dot"></span>www.brindlesports.example</div>
    <div class="footer__info">info@brindlesports.example &nbsp;|&nbsp; 418 Cedar Ridge Road, Pine Hollow, Texas 75000 &nbsp;|&nbsp; (555) 010 2468</div>
  </footer>
</section>

</body>
</html>
```